Business Card cabinets and cabinets components making company.

the card should be formal and interesting at the same time. The main colors will be black and white.

Font styles to use
Sans Serif

Colors

Designer to choose only greyscale colors for use in the design.

Requirements
Must have
• At least must have the followings:
office phone
cell phone
address
position
name
email
web

```html
<!DOCTYPE html>
<html lang="en">
<head>
<meta charset="utf-8">
<title>Panelcraft Business Card</title>
<link href="https://fonts.googleapis.com/css2?family=Roboto:wght@400;500;700&display=swap" rel="stylesheet">
<style>
  :root {
    --page: #c9c9c9;
    --white: #ffffff;
    --ink: #1e1e1e;
    --text: #2b2b2b;
    --mid-grey: #bcbcbc;
    --light-grey: #d3d3d3;
    --dark: #1f1f1f;
  }
  * { margin: 0; padding: 0; box-sizing: border-box; }
  html, body {
    width: 1125px; height: 1200px; overflow: hidden;
    background: var(--page);
    font-family: "Roboto", Arial, sans-serif;
  }
  .card {
    position: absolute;
    left: 151px;
    width: 825px;
    height: 472px;
    border-radius: 22px;
    overflow: hidden;
    box-shadow: 0 3px 8px rgba(0,0,0,0.25);
  }
  .card--front { top: 98px; background: var(--white); }
  .card--back { top: 631px; background: var(--mid-grey); }

  .cabinet-art {
    position: absolute; left: 0; top: 0; bottom: 0;
  }
  .card--front .cabinet-art {
    width: 298px;
    background: linear-gradient(90deg, var(--light-grey) 0%, #9a9a9a 45%, var(--dark) 100%);
  }
  .card--back .cabinet-art {
    width: 333px;
    background: linear-gradient(90deg, var(--dark) 0%, #3a3a3a 40%, #e9e9e9 75%, var(--mid-grey) 100%);
  }
  .base-band {
    position: absolute; left: 278px; right: 0; bottom: 0;
    height: 12px; background: var(--dark);
  }

  .wordmark {
    position: absolute;
    display: flex; align-items: center; gap: 12px;
    font-weight: 700;
    color: var(--ink);
    letter-spacing: -1px;
    line-height: 1;
  }
  .wordmark__square {
    width: 22px; height: 22px; background: var(--ink);
  }
  .card--front .wordmark { left: 447px; top: 50px; font-size: 60px; }
  .card--back .wordmark { left: 434px; top: 268px; font-size: 70px; }

  .contact { position: absolute; left: 447px; top: 160px; color: var(--text); }
  .contact__name { font-size: 29px; font-weight: 500; color: var(--ink); line-height: 1.1; }
  .contact__role { font-size: 22px; margin-top: 4px; }
  .contact__address { font-size: 21px; line-height: 27px; margin-top: 14px; }
  .contact__list { list-style: none; margin-top: 12px; }
  .contact__list li {
    display: flex; align-items: center; gap: 14px;
    font-size: 21px; height: 28px;
  }
  .contact__list svg { width: 18px; height: 18px; fill: var(--ink); flex: none; }

  .back-web {
    position: absolute; left: 385px; width: 420px; top: 410px;
    text-align: center; font-size: 21px; color: var(--text);
  }
</style>
</head>
<body>

<section class="card card--front">
  <div class="cabinet-art" role="img" aria-label="Large stylised drawing of a cabinet with open drawers in black, white and grey"></div>
  <div class="base-band"></div>

  <div class="wordmark"><span>Panelcraft</span><span class="wordmark__square"></span></div>

  <div class="contact">
    <p class="contact__name">Daniel Brooks</p>
    <p class="contact__role">Manager</p>
    <p class="contact__address">48 Timber Lane, Ashford<br>OH, ZIP 44012</p>
    <ul class="contact__list">
      <li>
        <svg viewBox="0 0 24 24" aria-hidden="true"><path d="M6.6 10.8c1.4 2.8 3.8 5.1 6.6 6.6l2.2-2.2c.3-.3.7-.4 1-.2 1.1.4 2.3.6 3.6.6.6 0 1 .4 1 1V20c0 .6-.4 1-1 1C10.6 21 3 13.4 3 4c0-.6.4-1 1-1h3.5c.6 0 1 .4 1 1 0 1.3.2 2.5.6 3.6.1.3 0 .7-.2 1z"/></svg>
        <span>555-318-4207</span>
      </li>
      <li>
        <svg viewBox="0 0 24 24" aria-hidden="true"><path d="M7 2h10a2 2 0 0 1 2 2v16a2 2 0 0 1-2 2H7a2 2 0 0 1-2-2V4a2 2 0 0 1 2-2zm0 3v13h10V5zm5 14.2a1 1 0 1 0 0 .1z"/></svg>
        <span>555-742-1986</span>
      </li>
      <li>
        <svg viewBox="0 0 24 24" aria-hidden="true"><path d="M3 5h18v14H3zm2 2v.5l7 4.5 7-4.5V7zm0 2.9V17h14V9.9l-7 4.5z"/></svg>
        <span>daniel@panelcraft.com</span>
      </li>
      <li>
        <svg viewBox="0 0 24 24" aria-hidden="true"><path d="M12 2a10 10 0 1 0 0 20 10 10 0 0 0 0-20zm6.9 9h-3c-.1-2.3-.6-4.4-1.4-5.9A8 8 0 0 1 18.9 11zM12 4c.9 1.1 1.8 3.6 1.9 7h-3.8c.1-3.4 1-5.9 1.9-7zM9.5 5.1C8.7 6.6 8.2 8.7 8.1 11h-3a8 8 0 0 1 4.4-5.9zM5.1 13h3c.1 2.3.6 4.4 1.4 5.9A8 8 0 0 1 5.1 13zM12 20c-.9-1.1-1.8-3.6-1.9-7h3.8c-.1 3.4-1 5.9-1.9 7zm2.5-1.1c.8-1.5 1.3-3.6 1.4-5.9h3a8 8 0 0 1-4.4 5.9z"/></svg>
        <span>www.panelcraftco.com</span>
      </li>
    </ul>
  </div>
</section>

<section class="card card--back">
  <div class="cabinet-art" role="img" aria-label="Large stylised drawing of a cabinet with open drawers in black and white"></div>
  <div class="wordmark"><span>Panelcraft</span><span class="wordmark__square"></span></div>
  <p class="back-web">www.panelcraftco.com</p>
</section>

</body>
</html>
```